CREATIVE DESIGNERS NEEDED & Enhance Your Business Card Portfolio

Artistic, unique, professional real estate card needed - see attached documents "B-cards.pdf" for all details and examples.True Designers will see other projects of ours come online here. We like long-term relationships for creative designers. This business card will be used in two U.S. states and is central to our business and other future marketing.

Target Market(s)

Buyers and Sellers of real estate

Industry/Entity Type

Real Estate Agent

Contact Information for Business Card

See attached detailed brief

Other font styles liked:
• ADAM.CG PRO & NewsGoth BT

Requirements
Must have
• 2-sided, creative (non-traditional layout/design). Incorporate a cut-out (for texture, and make it fun! No boring templates for this card -
Nice to have
• See attached detailed brief
Should not have

```html
<!DOCTYPE html>
<html lang="en">
<head>
<meta charset="utf-8">
<title>Harlow Crest Group – Business Card</title>
<link rel="stylesheet" href="https://fonts.googleapis.com/css2?family=Montserrat:wght@400;600;700;800&family=Roboto:wght@300;400&display=swap">
<style>
  :root {
    --navy: #26374a;
    --red: #c8202a;
    --white: #ffffff;
    --ink: #3a3f47;
    --stage: #4a423b;
  }
  * { box-sizing: border-box; margin: 0; padding: 0; }
  html, body { width: 1200px; height: 930px; overflow: hidden; }
  body { background: var(--stage); position: relative; font-family: "Roboto", sans-serif; }

  .card {
    position: absolute;
    width: 560px; height: 320px;
    border-radius: 16px;
    overflow: hidden;
    box-shadow: 0 10px 28px rgba(0,0,0,.35);
  }

  /* Front */
  .card-front { left: 90px; top: 90px; background: var(--navy); color: var(--white); }
  .front-brand {
    position: absolute; left: 0; right: 0; top: 98px;
    display: flex; align-items: center; justify-content: center; gap: 16px;
  }
  .brand-square { width: 58px; height: 58px; background: var(--white); }
  .brand-name { font-family: "Montserrat", sans-serif; font-weight: 700; line-height: 1; }
  .brand-name .first { font-size: 44px; letter-spacing: 1px; display: block; }
  .brand-name .rest { font-size: 17px; letter-spacing: 1px; display: block; margin-top: 4px; }
  .brand-name .sub { font-size: 12px; font-weight: 400; letter-spacing: 7px; display: block; margin-top: 3px; }
  .front-cities {
    position: absolute; left: 0; right: 0; top: 228px;
    text-align: center; font-family: "Montserrat", sans-serif;
    font-size: 19px; letter-spacing: 2px;
  }

  /* Back */
  .card-back { left: 530px; top: 520px; background: var(--white); color: var(--ink); }
  .back-tab { position: absolute; left: 0; top: 0; }
  .photo {
    position: absolute; left: 64px; top: 50px;
    width: 156px; height: 156px; border-radius: 50%;
    border: 3px solid var(--navy);
    box-shadow: 0 0 0 6px var(--white);
    background: radial-gradient(circle at 50% 45%, #d9a98f 0 30%, #6a5146 55%, #e7e3df 80%);
  }
  .back-brand {
    position: absolute; right: 28px; top: 22px;
    display: flex; align-items: center; gap: 10px; color: var(--navy);
  }
  .back-brand .brand-square { width: 40px; height: 40px; background: var(--red); }
  .back-brand .first { font-size: 30px; }
  .back-brand .rest { font-size: 12px; }
  .back-brand .sub { font-size: 9px; letter-spacing: 5px; color: var(--red); }

  .partners {
    position: absolute; right: 28px; top: 92px;
    display: flex; align-items: center; gap: 12px;
  }
  .partner-name { font-family: "Montserrat", sans-serif; font-weight: 600; font-size: 16px; color: var(--red); }
  .partner-mark { width: 14px; height: 14px; background: var(--red); }
  .badge { width: 24px; height: 22px; background: var(--navy); }
  .badge.wide { width: 38px; height: 18px; background: #8a9099; }

  .agent { position: absolute; right: 28px; top: 124px; text-align: right; }
  .agent-name { font-family: "Montserrat", sans-serif; font-weight: 800; font-size: 26px; color: var(--red); letter-spacing: .5px; line-height: 1.2; }
  .agent-title { font-size: 12px; color: var(--ink); margin-top: 2px; }

  .rule { position: absolute; height: 1px; background: var(--red); }
  .rule-right { left: 236px; right: 28px; top: 178px; }
  .rule-left { left: 30px; width: 206px; top: 222px; }

  .address {
    position: absolute; right: 28px; top: 188px;
    text-align: right; font-size: 12px; line-height: 1.5; color: var(--ink);
  }

  .contacts { position: absolute; left: 30px; top: 230px; list-style: none; }
  .contacts li { display: flex; align-items: center; gap: 8px; font-size: 13px; line-height: 1.5; color: var(--ink); }
  .contacts svg { width: 10px; height: 10px; flex: none; }
</style>
</head>
<body>

  <section class="card card-front">
    <div class="front-brand">
      <span class="brand-square"></span>
      <div class="brand-name">
        <span class="first">HARLOW</span>
        <span class="rest">CREST GROUP</span>
        <span class="sub">REAL ESTATE</span>
      </div>
    </div>
    <p class="front-cities">SPRINGFIELD - FAIRVIEW</p>
  </section>

  <section class="card card-back">
    <svg class="back-tab" width="230" height="170" viewBox="0 0 230 170" aria-hidden="true">
      <polygon points="30,0 196,0 216,60 170,60 120,170 30,170" fill="var(--navy)"/>
    </svg>
    <div class="photo" role="img" aria-label="Portrait photo of the agent"></div>

    <div class="back-brand">
      <span class="brand-square"></span>
      <div class="brand-name">
        <span class="first">HARLOW</span>
        <span class="rest">CREST GROUP</span>
        <span class="sub">REAL ESTATE</span>
      </div>
    </div>

    <div class="partners">
      <span class="partner-mark"></span>
      <span class="partner-name">Keystone</span>
      <span class="badge"></span>
      <span class="badge wide"></span>
    </div>

    <div class="agent">
      <h1 class="agent-name">DEAN HARLOW</h1>
      <p class="agent-title">Broker Associate &amp; Sales Agent</p>
    </div>

    <div class="rule rule-right"></div>
    <div class="rule rule-left"></div>

    <p class="address">410 Laurel Avenue Springfield,<br>CA 90210 &amp; 2280 W.<br>Cedar Rd #B Fairview, AZ 85000</p>

    <ul class="contacts">
      <li><svg viewBox="0 0 10 10"><path d="M2 1l2 2-1 1.2a5 5 0 0 0 2.8 2.8L7 6l2 2-1.4 1.4C4.5 9 1 5.5.6 2.4z" fill="var(--red)"/></svg>(855) BUY-HOME</li>
      <li><svg viewBox="0 0 10 10"><rect x="2.5" y=".5" width="5" height="9" rx="1" fill="none" stroke="var(--red)"/><circle cx="5" cy="8" r=".6" fill="var(--red)"/></svg>(555) 014-2280</li>
      <li><svg viewBox="0 0 10 10"><rect x=".5" y="2" width="9" height="6" fill="none" stroke="var(--red)"/><path d="M.5 2l4.5 3.5L9.5 2" fill="none" stroke="var(--red)"/></svg>Dean@HarlowCrestGroup.com</li>
      <li><svg viewBox="0 0 10 10"><circle cx="5" cy="5" r="4.4" fill="none" stroke="var(--red)"/><path d="M.6 5h8.8M5 .6c2 2.5 2 6.3 0 8.8M5 .6c-2 2.5-2 6.3 0 8.8" fill="none" stroke="var(--red)" stroke-width=".8"/></svg>HarlowCrestRealEstate</li>
    </ul>
  </section>

</body>
</html>
```